Capability Statement for Consulting firm to effectively market skills to Government buyers and pr...

We need a ONE PAGE capability statement document that is visually interesting and has similar design/graphic elements to my logo and website. A Capability Statement should also show a firm's logo and other branding elements for recognition and be free of long paragraphs, instead, using short sentences and bulleted lists for quick visual scanning.<br/>The five key areas included in a successful Capability Statement are:<br/>1. Core competencies / capabilities<br/>2. Differentiators / including facilities and equipment<br/>3. Past performance<br/>4. Corporate data including industry codes<br/>5. Contact information<br/>The five key areas included in a successful Capability Statement are:<br/>1. Core competencies / capabilities<br/>2. Differentiators / including facilities and equipment<br/>3. Past performance<br/>4. Corporate data including industry codes<br/>5. Contact information<br/>When composing a Capability Statement, use the following section labels: Core Competencies,<br/>Past Performance, and Differentiators. These are the key elements that government buyers are<br/>looking for so that they can make a speedy decision.<br/>1. Core Competencies<br/>These are short introduction statements relating the company's core competencies to the agency's<br/>specific needs followed by key-word heavy bullet points. This is NOT everything a firm is able<br/>to do, but the core expertise of a firm, specifically related to the agency this Capability Statement<br/>is written for, its mission and identified opportunities.<br/>2. Differentiators<br/>Doing business with the government is highly competitive. Contractors have the burden of<br/>dealing with this competitive market and rising above the other contractors. Many companies<br/>who are trying to increase sales to the government market do not have a clear value statement<br/>detailing what makes them different from their competitors. A succinct, clear statement that<br/>relates to the specific needs of the agency is what will help the procurement and purchasing staff,<br/>the program managers and end users understand why they should pick your firm over other<br/>competitors.<br/>Sample Differentiator Questions:<br/>How is your company best suited for the needs of this agency? What is it about your services that<br/>make you stand out from the rest? What is it about your people that give you the advantage over<br/>your competitors? Why are your products better solutions than the others that are available?<br/>If these benefits cannot be clearly communicated, it is impossible for a decision-maker to make a<br/>clear recommendation for your company over one of your competitors. Many companies fail to<br/>take this critical step. And they wonder why they are missing out on contracts.<br/>3. Past Performance<br/>Begin by listing past customers for whom your business has done similar work. Prioritize<br/>starting with related agency, to all federal to other government, to commercial contracts. If the<br/>past projects do not relate to the targeted agency's needs, do not list it.<br/>Tip: Ideally, include specific contact information for immediate references. Include<br/>name, title, email and phone. Use this information when meeting with decision-makers.<br/>Leave this information off the Capability Statement when you are sending the PDF as an<br/>initial outreach effort or leaving as a handout at conferences.<br/>4. Company Data<br/>Include one or two short sentences with a company description detailing pertinent history.<br/>Include the size of your firm, your revenue, the number of employees you have, and the typical<br/>geographic area you serve.<br/>Show contact information, including web site and a specific person's name, email and phone<br/>number, on each side or page of the document.<br/>If your firm has won any awards, received accolades or has notable accomplishments relating to<br/>that agency, list them only if you have space.<br/>Using this information will help in creating a Powerful Capability Statement and open doors to<br/>contracting opportunities in the federal government. This document is the key to building<br/>relationship with important decision-makers in government contracting, providing them with a<br/>concise description of the goods and services your business can provide, and a consistent<br/>reminder of your firm.<br/><br/>Logo must be prominently on top of page<br/><br/>Should be ONE PAGE

Target Market(s)

Government buyers and Prime Contractors

Other font styles liked:
• Be Creative

Colors

Designer to choose colors to be used in the design.

Requirements
Must have
• Be ONE PAGE-BE consistent with branding elements of my webpage
• all of the data and elements provided on the MS Word document
• I must be able to edit the document as needed
• My logo is in the MS word document
Nice to have
• visually compelling document that will attract buyers and concisely present my capabilities.
• Modern and chic
• Girls should want to hang on their and guys should want to emulate
Should not have
• Not more than one page
• copy of other business
• boring and dull

```html
<!DOCTYPE html>
<html lang="en">
<head>
<meta charset="utf-8">
<title>Kestrel Project Advisors – Capability Statement</title>
<link href="https://fonts.googleapis.com/css2?family=Montserrat:wght@400;500;600&family=Roboto:wght@300;400;900&display=swap" rel="stylesheet">
<style>
  :root {
    --orange: #f7931e;
    --ink: #3f3f3f;
    --muted: #555555;
    --dark: #3a3a3c;
    --darker: #2b2b2d;
    --sky: #b9cfe0;
    --backdrop: #d6d6d6;
    --white: #ffffff;
  }
  * { box-sizing: border-box; margin: 0; padding: 0; }
  html, body { width: 703px; height: 1200px; overflow: hidden; }
  body {
    background: var(--backdrop);
    font-family: "Montserrat", Arial, sans-serif;
    color: var(--ink);
  }
  .page {
    position: absolute; left: 0; top: 103px;
    width: 703px; height: 993px;
    background: var(--white);
    overflow: hidden;
    box-shadow: 0 4px 14px rgba(0,0,0,.18);
  }

  /* Header */
  .hero { position: absolute; left: 0; top: 0; width: 703px; height: 345px; }
  .hero-photo {
    position: absolute; inset: 0;
    background: linear-gradient(180deg, #bcd1e2 0%, #9fb0bd 45%, #8a6a4e 78%, #5a4536 100%);
  }
  .hero-shade { position: absolute; inset: 0; }
  .brand {
    position: absolute; left: 30px; top: 58px; width: 140px;
    display: flex; flex-direction: column; align-items: center; gap: 8px;
  }
  .brand-dot { width: 22px; height: 22px; border-radius: 50%; background: var(--darker); }
  .brand-name {
    font-family: "Montserrat", Arial, sans-serif; font-weight: 600;
    font-size: 13px; letter-spacing: 1px; color: var(--darker);
    text-align: center; line-height: 1.25; text-transform: uppercase;
  }
  .headline {
    position: absolute; left: 352px; top: 76px;
    font-family: "Roboto", Arial, sans-serif; color: var(--white);
    line-height: 42px;
  }
  .headline .strong { font-weight: 900; color: var(--orange); font-size: 44px; display: block; }
  .headline .light { font-weight: 300; font-size: 37px; display: block; }

  /* Columns */
  .column { position: absolute; top: 360px; }
  .column-left { left: 46px; width: 262px; }
  .column-right { left: 385px; width: 278px; }
  .section-title {
    font-family: "Roboto", Arial, sans-serif; font-weight: 900;
    color: var(--orange); font-size: 17px; line-height: 19px;
    margin-bottom: 12px; letter-spacing: .2px;
  }
  p.copy {
    font-size: 9.1px; line-height: 11.4px; color: var(--muted);
    text-align: justify; margin-bottom: 8px;
  }
  .tick-list { list-style: none; }
  .tick-list li {
    position: relative; padding-left: 21px;
    font-size: 9.1px; line-height: 11.4px; color: var(--muted);
  }
  .tick-list li svg { position: absolute; left: 0; top: 1px; width: 10px; height: 10px; }
  .tick-list .label { color: var(--orange); }
  .competencies { margin-top: 22px; }
  .competencies li { margin-bottom: 10px; }
  .performance li { margin-bottom: 10px; }
  .codes li { margin-bottom: 4px; }
  .block { margin-bottom: 22px; }

  .diff-list { list-style: none; margin-bottom: 18px; }
  .diff-list li {
    display: flex; align-items: center; gap: 12px;
    font-size: 9.1px; line-height: 11.4px; font-weight: 600; color: var(--ink);
    margin-bottom: 8px; min-height: 22px;
  }
  .diff-list svg { flex: 0 0 21px; width: 21px; height: 21px; }

  /* Footer */
  .footer { position: absolute; left: 0; top: 939px; width: 703px; height: 54px; }
  .footer svg.band { position: absolute; inset: 0; }
  .contact-name {
    position: absolute; left: 136px; top: 10px;
    font-family: "Roboto", Arial, sans-serif; font-weight: 900;
    color: var(--orange); font-size: 15px; line-height: 16px;
  }
  .contact-role { position: absolute; left: 136px; top: 27px; font-size: 8px; color: var(--white); }
  .contact-line {
    position: absolute; font-size: 8px; color: var(--white);
    display: flex; align-items: center; gap: 4px; white-space: nowrap;
  }
  .contact-line .cta { color: var(--orange); }
  .contact-line svg { width: 8px; height: 8px; }
</style>
</head>
<body>
<svg width="0" height="0" style="position:absolute">
  <defs>
    <symbol id="tick" viewBox="0 0 10 10">
      <path d="M8.2 3.2A4 4 0 1 1 6.6 1.6" fill="none" stroke="#3f3f3f" stroke-width="1"/>
      <path d="M2.8 4.8l2 2L9.3 1.8" fill="none" stroke="#3f3f3f" stroke-width="1.2"/>
    </symbol>
  </defs>
</svg>

<main class="page">
  <header class="hero">
    <div class="hero-photo" role="img" aria-label="City skyline with glass towers at sunset"></div>
    <svg class="hero-shade" viewBox="0 0 703 345" preserveAspectRatio="none" aria-hidden="true">
      <polygon points="145,0 703,0 703,345 270,345" fill="#2f2f31" opacity=".72"/>
      <polygon points="145,0 703,0 703,73 190,73" fill="#555" opacity=".45"/>
    </svg>
    <div class="brand">
      <span class="brand-dot"></span>
      <span class="brand-name">Kestrel<br>Project Advisors</span>
    </div>
    <h1 class="headline">
      <span class="strong">WE UNCOVER</span>
      <span class="light">and Implement the</span>
      <span class="strong">Right Solution</span>
      <span class="light">at the Right Time</span>
      <span class="light">in the Right Way</span>
    </h1>
  </header>

  <section class="column column-left">
    <div class="block">
      <h2 class="section-title">CORE COMPETENCIES</h2>
      <p class="copy">Kestrel Project Advisors specializes in custom-designed business strategy and project management solutions. We apply Global Project Standards Board (GPSB) principles to offer technically and commercially sound solutions for government agencies, manufacturing/industrial facilities, power generation plants, water treatment, and commercial strategy.</p>
      <ul class="tick-list competencies">
        <li><svg><use href="#tick"/></svg><span class="label">Photovoltaic Application Solutions:</span> expertise in technical design, procurement, and construction to deliver all phases of solar farm construction.</li>
        <li><svg><use href="#tick"/></svg><span class="label">Project Management Expertise:</span> reduce costs, manage risk, and optimize safety.</li>
        <li><svg><use href="#tick"/></svg><span class="label">International Experience and Support:</span> resolve complex problems utilizing our global project experience and resources</li>
        <li><svg><use href="#tick"/></svg><span class="label">Commercial Strategy:</span> operate safer and more cost effectively to maximize your profits</li>
      </ul>
    </div>
    <div class="block">
      <h2 class="section-title">PAST PERFORMANCE</h2>
      <ul class="tick-list performance">
        <li><svg><use href="#tick"/></svg><span class="label">Solvanta</span> - Meridian Generating Station. We provided engineering, 3D modelling, and engineered pipe supports for a $2 Billion 280 MW solar facility, which was the largest parabolic trough plant in the world. Our engineered pipe supports reduced downtime and reduced maintenance costs as an employee of Forge Industrial.</li>
        <li><svg><use href="#tick"/></svg><span class="label">Al Noor Group</span>- Saudi Arabia Designed, manufactured, and commissioned API 675 compliant chemical injection metering skids that reduced costs via precise chemical dosing for multi-million-dollar industrial water treatment project as an employee of Praxis corporation.</li>
        <li><svg><use href="#tick"/></svg><span class="label">PetroNova</span>- Baytown and Beaumont Designed, manufactured, and project managed ASME B31.1 compliant custom engineered pipe support systems as an employee of Forge Industrial.</li>
      </ul>
    </div>
  </section>

  <section class="column column-right">
    <h2 class="section-title">DIFFERENTIATORS</h2>
    <ul class="diff-list">
      <li>
        <svg viewBox="0 0 22 22"><circle cx="11" cy="11" r="10" fill="none" stroke="#f7931e" stroke-width="1.2"/><circle cx="11" cy="11" r="5" fill="none" stroke="#f7931e"/><path d="M11 8v3h2.5" fill="none" stroke="#f7931e"/></svg>
        24 Hour Commercial Quote Delivery Available
      </li>
      <li>
        <svg viewBox="0 0 22 22"><circle cx="11" cy="11" r="10" fill="none" stroke="#f7931e" stroke-width="1.2"/><rect x="5" y="8" width="8" height="5" fill="#f7931e"/><path d="M13 9h3l2 2v2h-5z" fill="#f7931e"/><circle cx="8" cy="14.5" r="1.3" fill="#f7931e"/><circle cx="15.5" cy="14.5" r="1.3" fill="#f7931e"/></svg>
        Involved with first U.S. solar plant with molten<br>salt thermal energy storage
      </li>
      <li>
        <svg viewBox="0 0 22 22"><circle cx="11" cy="11" r="10" fill="none" stroke="#f7931e" stroke-width="1.2"/><rect x="6" y="11" width="2.5" height="5" fill="#f7931e"/><rect x="9.8" y="8" width="2.5" height="8" fill="#f7931e"/><rect x="13.6" y="6" width="2.5" height="10" fill="#f7931e"/></svg>
        Experienced in waste water, industrial, and<br>municipal water treatment
      </li>
      <li>
        <svg viewBox="0 0 22 22"><circle cx="11" cy="11" r="10" fill="none" stroke="#f7931e" stroke-width="1.2"/><path d="M14.5 6.5H7.5l4 4.5-4 4.5h7" fill="none" stroke="#f7931e" stroke-width="1.2"/></svg>
        Lean Six Sigma capabilities
      </li>
    </ul>

    <div class="block">
      <h2 class="section-title">COMPANY DATA</h2>
      <p class="copy">Kestrel Project Advisors was formed with the intent of optimizing operations, streamlining project management, and maximizing value creation to best help public and private sector clients turn areas of stagnation into growth.</p>
      <p class="copy">This ethos continues to lie at the core of our firm.</p>
      <p class="copy">We are the consulting firm recognized for asking thorough questions, actively listening, and working relentlessly until the goals are achieved. We are fact-driven and action-oriented. We move our clients forward, to where they need to be.</p>
    </div>

    <h2 class="section-title">LIST OF SPECIFIC PERTINENT<br>CODES AND DATA</h2>
    <ul class="tick-list codes">
      <li><svg><use href="#tick"/></svg>Kestrel Project Advisors</li>
      <li><svg><use href="#tick"/></svg>DUNS # holder</li>
      <li><svg><use href="#tick"/></svg>CAGE Code holder</li>
      <li><svg><use href="#tick"/></svg><span class="label">NAICS Codes:</span> 541611, 221114, 237130, 238160, 238210, 611430, 611699, 541613, 541614, 541612, 541810, 541990</li>
      <li><svg><use href="#tick"/></svg><span class="label">NIGP Codes:</span> 918-49, 962-58, 918-79, 918-58, 925-53, 918-42, 915-22, 961-56, 958-77, 918-79, 918-76, 918-38, 915-01, 918-07, 209-69, 208-68, 918-35, 918-20, 918-06</li>
      <li><svg><use href="#tick"/></svg>Accept Credit Cards</li>
      <li><svg><use href="#tick"/></svg>Socio-economic status holder</li>
    </ul>
  </section>

  <footer class="footer">
    <svg class="band" viewBox="0 0 703 54" preserveAspectRatio="none" aria-hidden="true">
      <rect x="0" y="46" width="703" height="8" fill="#bdbdbd"/>
      <polygon points="128,0 703,0 703,54 92,54" fill="#3a3a3c"/>
      <polygon points="75,18 90,18 64,54 49,54" fill="#f7931e"/>
      <polygon points="96,18 111,18 85,54 70,54" fill="#f7931e"/>
    </svg>
    <div class="contact-name">Daniel Whitmore</div>
    <div class="contact-role">VP of Project Management</div>
    <div class="contact-line" style="left:282px; top:13px;"><span class="cta">CALL US NOW:</span>&nbsp;(555) 318 -2046</div>
    <div class="contact-line" style="left:282px; top:27px;">
      <svg viewBox="0 0 8 8"><path d="M4 0a3 3 0 0 1 3 3c0 2-3 5-3 5S1 5 1 3a3 3 0 0 1 3-3z" fill="#f7931e"/><circle cx="4" cy="3" r="1" fill="#3a3a3c"/></svg>
      410 Harbor Ave, Suite 900 Houston, TX
    </div>
    <div class="contact-line" style="left:454px; top:13px;">
      <svg viewBox="0 0 8 8"><rect x="0.5" y="1.5" width="7" height="5" fill="none" stroke="#f7931e"/><path d="M.5 1.5l3.5 3 3.5-3" fill="none" stroke="#f7931e"/></svg>
      dwhitmore@kestrelprojectadvisors.com
    </div>
    <div class="contact-line" style="left:454px; top:27px;">
      <svg viewBox="0 0 8 8"><circle cx="4" cy="4" r="3.4" fill="none" stroke="#f7931e"/><path d="M.6 4h6.8M4 .6c-2 2-2 4.8 0 6.8M4 .6c2 2 2 4.8 0 6.8" fill="none" stroke="#f7931e" stroke-width=".7"/></svg>
      www.kestrelprojectadvisors.com
    </div>
  </footer>
</main>
</body>
</html>
```